Craft brewery website - Harrow Lane Brewery

Looking for a simple site similar to fennimoorales.com or tallwharf.com with the following features:
- incorporates existing logo (file attached)
- has a consistent look and feel throughout the site that works in harmony with the logo. Please suggest a cool font to use!
- incorporates all or some of the attached images
- has the following tabs/pages: home, our story, brews, blog, contact.
- has some sort of prominent image/design under the top menu bar that can be updated with content - so a placeholder for text. Please use this text on home page: "we brew up our passion for honest ingredients, our curiosity for different cultures, and social and environmental consciousness into characteristic beers." And "Beers with a Twist for the good of the world, for the fun of the party"
- has a scrolling set of images under main section that will list beers. Please create five placeholders for beers: Weizenbock, Wandering Heron, Stout, Saison, Dusty Hal

Industry/Entity Type

Brewery

Number of Pages Required

1 page

Requirements
Must have
• Looking for a simple site similar to fennimoorales.com with the following features:
• - incorporates existing logo (file attached)
• - has a consistent look and feel throughout the site that works in harmony with the logo. Please suggest a cool font to use!
• - incorporates all or some of the attached images
• - has the following tabs/pages: home, our story, brews, blog, contact.
• - has some sort of prominent image/design under the top menu bar that can be updated with content - so a placeholder for text. Please use this text on home page: "we brew up our passion for honest ingredients, our curiosity for different cultures, and social and environmental consciousness into characteristic beers." And "Beers with a Twist for the good of the world, for the fun of the party"
• - has a scrolling set of images under main section that will list beers. Please create five placeholders for beers: Weizenbock, Wandering Heron, Stout, Saison, Dusty Hal

```html
<!DOCTYPE html>
<html lang="en">
<head>
<meta charset="utf-8">
<title>Harrow Lane Brewery</title>
<link rel="stylesheet" href="https://fonts.googleapis.com/css2?family=Oswald:wght@400;500;600&family=Open+Sans:wght@400;600;700&display=swap">
<style>
:root{
  --gold:#c08a2c;
  --gold-dark:#a8781f;
  --paper:#efede8;
  --paper-alt:#f3f1ec;
  --white:#fdfdfc;
  --ink:#2a2a2a;
  --muted:#777;
  --footer:#232323;
  --footer-text:#e8e8e8;
  --hero-a:#5c5a55;
  --hero-b:#8d8a82;
}
*{margin:0;padding:0;box-sizing:border-box}
html,body{width:1200px;height:3358px;overflow:hidden}
body{position:relative;background:var(--paper);font-family:"Open Sans",Arial,sans-serif;color:var(--ink)}
.display{font-family:"Oswald","Arial Narrow",sans-serif;text-transform:uppercase;color:var(--gold);font-weight:500;letter-spacing:.5px}
.btn{position:absolute;background:var(--gold-dark);color:#fff;font-family:"Oswald","Arial Narrow",sans-serif;text-transform:uppercase;font-weight:500;display:flex;align-items:center;justify-content:center;font-size:19px}
.rule{position:absolute;left:0;width:1200px;height:3px;background:var(--gold)}

/* header */
.site-header{position:absolute;top:0;left:0;width:1200px;height:168px;background:var(--paper)}
.topbar{position:absolute;top:34px;right:103px;font-size:15px;color:#333;display:flex;gap:22px;align-items:center;white-space:nowrap}
.topbar span{display:flex;align-items:center;gap:8px}
.main-nav{position:absolute;top:100px;right:100px;display:flex;gap:33px}
.main-nav a{font-family:"Oswald","Arial Narrow",sans-serif;font-weight:500;font-size:27px;color:var(--gold);text-decoration:none;text-transform:uppercase}
.brand{position:absolute;left:100px;top:22px;width:200px;height:212px;border-radius:50%;background:var(--paper);border:6px solid var(--gold);display:flex;align-items:center;justify-content:center;text-align:center;z-index:3;font-family:"Oswald","Arial Narrow",sans-serif;font-weight:500;color:var(--gold);font-size:28px;line-height:1.1;text-transform:uppercase;padding:20px}

/* hero */
.hero{position:absolute;top:168px;left:0;width:1200px;height:544px;background:linear-gradient(120deg,var(--hero-a),var(--hero-b) 60%,#6d6a62)}
.hero-kicker{position:absolute;left:98px;top:132px;font-family:"Oswald",sans-serif;font-weight:500;font-size:34px;color:#fff;text-transform:uppercase;white-space:nowrap}
.hero-title{position:absolute;left:98px;top:182px;font-size:60px;line-height:1.1;white-space:nowrap}
.hero-text{position:absolute;left:98px;top:272px;width:520px;font-size:16px;font-weight:700;color:#fff;line-height:1.6}
.hero .btn{left:98px;top:358px;width:180px;height:50px}
.hero-arrow{position:absolute;top:250px}

/* welcome */
.welcome{position:absolute;top:715px;left:0;width:1200px;height:653px;background:var(--paper-alt)}
.welcome h1{position:absolute;top:54px;width:1200px;text-align:center;font-size:42px;line-height:1.2}
.welcome .underline{position:absolute;top:128px;left:493px;width:215px;height:5px;background:#8f7840}
.welcome p{position:absolute;top:178px;left:110px;width:980px;text-align:center;font-size:15px;line-height:1.9;color:#333}
.brews{position:absolute;top:315px;left:0;width:1200px;height:230px}
.brew-divider{position:absolute;top:0;width:3px;height:224px;background:var(--gold)}
.brew{position:absolute;top:5px;width:190px;text-align:center}
.brew .shot{width:152px;height:152px;border-radius:50%;margin:0 auto;border:5px solid #cdb582;background:linear-gradient(160deg,#b8a88a,#6a4a2e)}
.brew h3{margin-top:30px;font-size:21px;white-space:nowrap}

/* events */
.events{position:absolute;top:1371px;left:0;width:1200px;height:539px;background:var(--white)}
.events h2{position:absolute;left:98px;top:52px;font-size:40px;line-height:1.2}
.events p{position:absolute;left:98px;top:135px;width:430px;font-size:17px;line-height:1.75;color:#222}
.events .btn{left:98px;top:225px;width:188px;height:52px}
.hours{position:absolute;left:98px;top:310px;font-family:"Oswald",sans-serif;font-size:19px;color:var(--gold);line-height:36px;text-transform:uppercase;white-space:nowrap}
.events .art{position:absolute;left:638px;top:30px;width:392px;height:470px;background:linear-gradient(160deg,#e8e6e2,#8a93c0 40%,#3a3a48);border-radius:6px}

/* shop */
.shop{position:absolute;top:1913px;left:0;width:1200px;height:492px;background:var(--paper-alt)}
.shop .art{position:absolute;left:63px;top:69px;width:492px;height:336px;background:linear-gradient(150deg,#e6e3de,#4a5aa8 55%,#2e2e33);border-radius:6px}
.shop h2{position:absolute;left:571px;top:78px;font-size:40px;line-height:1.2}
.shop p{position:absolute;left:571px;top:142px;width:530px;font-size:13.5px;line-height:1.85;text-align:justify;color:#222}
.shop .mugs{position:absolute;left:571px;top:255px;width:370px;height:138px;background:linear-gradient(90deg,#e9b12b,#c06a22 50%,#3f2618);border-radius:8px}

/* story + blog */
.stories{position:absolute;top:2408px;left:0;width:1200px;height:503px;background:var(--white)}
.stories h2{position:absolute;top:56px;font-size:32px;line-height:1.2}
.story-img{position:absolute;left:98px;top:122px;width:430px;height:231px;background:linear-gradient(140deg,#d8d5cf,#9c9890 50%,#6d4040)}
.story-text{position:absolute;left:98px;top:374px;width:435px;font-size:11.5px;line-height:1.9;color:#666}
.more{position:absolute;top:434px;font-size:12px;font-weight:700;color:var(--gold);text-transform:uppercase;white-space:nowrap}
.post{position:absolute;left:605px;width:495px;height:120px}
.post .thumb{position:absolute;left:0;top:0;width:152px;height:119px;background:linear-gradient(140deg,#d5d2cc,#7d7a74 60%,#3c3c48)}
.post h4{position:absolute;left:172px;top:0;font-family:"Open Sans",sans-serif;font-weight:600;font-size:13px;line-height:18px;color:#8a6418;white-space:nowrap}
.post .meta{position:absolute;left:172px;top:30px;font-size:11px;line-height:14px;color:#888;font-style:italic;display:flex;gap:22px;white-space:nowrap}
.post .excerpt{position:absolute;left:172px;top:56px;width:323px;font-size:11.5px;line-height:1.9;color:#666}
.post-sep{position:absolute;left:605px;width:495px;height:1px;background:#ddd}

/* footer */
.site-footer{position:absolute;top:2911px;left:0;width:1200px;height:447px;background:var(--footer);color:var(--footer-text)}
.site-footer h5{position:absolute;top:56px;font-size:24px;line-height:1.2;white-space:nowrap}
.site-footer .bar{position:absolute;top:100px;width:80px;height:2px;background:var(--gold)}
.f-about{position:absolute;left:98px;top:128px;width:320px;font-size:12.5px;line-height:2}
.f-links{position:absolute;left:443px;top:122px;list-style:none;font-size:14px;line-height:32px}
.f-contact{position:absolute;left:611px;top:128px}
.f-contact .row{position:relative;height:72px;padding-left:55px;font-size:12px;line-height:1.6}
.f-contact .row b{font-size:14px;display:block}
.f-contact svg{position:absolute;left:0;top:2px}
.f-news{position:absolute;left:873px;top:130px;font-size:14px}
.f-news .field{margin-top:20px;width:228px;height:38px;border:1px solid #ddd;border-radius:3px;font-size:12px;padding:10px 8px;color:#fff}
.f-news .sub{margin-top:14px;width:110px;height:36px;background:#d48a14;color:#fff;font-weight:700;font-size:12px;display:flex;align-items:center;justify-content:center}
.f-divider{position:absolute;left:98px;top:362px;width:1004px;height:1px;background:#555}
.copy{position:absolute;left:98px;top:392px;font-size:13px}
.social{position:absolute;left:872px;top:380px;display:flex;gap:12px}
.social span{width:40px;height:40px;border:2px solid #eee;border-radius:50%}
</style>
</head>
<body>

<header class="site-header">
  <div class="topbar">
    <span><svg width="14" height="11" viewBox="0 0 14 11"><rect x="0.5" y="0.5" width="13" height="10" fill="none" stroke="#333"/><path d="M1 1l6 5 6-5" fill="none" stroke="#333"/></svg>UNIT 4, MARLOW YARD 57, KILN ROAD</span>
    <span><svg width="12" height="12" viewBox="0 0 12 12"><path d="M2 1l3 0 1 3-2 1a7 7 0 0 0 3 3l1-2 3 1v3c-5 1-11-5-9-9z" fill="#333"/></svg>180 044 7193</span>
  </div>
  <nav class="main-nav">
    <a>Home</a><a>Our Story</a><a>Brews</a><a>Blog</a><a>Events</a><a>Shop</a><a>Contact</a>
  </nav>
</header>
<div class="brand">Harrow Lane Brewery</div>

<section class="hero" role="img" aria-label="Street mural of a kneeling archer drawing a bow, painted on a weathered wall">
  <div class="hero-kicker">We brew up our passion</div>
  <div class="hero-title display">Harrow Lane Brewery</div>
  <p class="hero-text">We brew up our passion for honest ingredients, our curiosity for different cultures.</p>
  <div class="btn">Contact here!</div>
  <svg class="hero-arrow" style="left:26px" width="30" height="60" viewBox="0 0 30 60"><path d="M27 2L3 30l24 28" fill="none" stroke="#fff" stroke-width="2"/></svg>
  <svg class="hero-arrow" style="left:1144px" width="30" height="60" viewBox="0 0 30 60"><path d="M3 2l24 28L3 58" fill="none" stroke="#fff" stroke-width="2"/></svg>
</section>
<div class="rule" style="top:712px"></div>

<section class="welcome">
  <h1 class="display">Welcome to Harrow Lane Brewery</h1>
  <div class="underline"></div>
  <p>we brew up our passion for honest ingredients, our curiosity for different cultures, and social and environmental consciousness into characteristic beers." And "Beers with a Twist for the good of the world, for the fun of the party"</p>
  <div class="brews">
    <div class="brew-divider" style="left:66px"></div>
    <div class="brew-divider" style="left:280px"></div>
    <div class="brew-divider" style="left:494px"></div>
    <div class="brew-divider" style="left:709px"></div>
    <div class="brew-divider" style="left:924px"></div>
    <div class="brew-divider" style="left:1138px"></div>
    <div class="brew" style="left:77px"><div class="shot" role="img" aria-label="Bottles of Weizenbock"></div><h3 class="display">Weizenbock</h3></div>
    <div class="brew" style="left:291px"><div class="shot" role="img" aria-label="Bottles of Wandering Heron"></div><h3 class="display">Wandering Heron</h3></div>
    <div class="brew" style="left:505px"><div class="shot" role="img" aria-label="Glass of stout"></div><h3 class="display">Stout</h3></div>
    <div class="brew" style="left:720px"><div class="shot" role="img" aria-label="Six-pack of saison"></div><h3 class="display">Saison</h3></div>
    <div class="brew" style="left:935px"><div class="shot" role="img" aria-label="Bottle and glass of Dusty Hal"></div><h3 class="display">Dusty Hal</h3></div>
  </div>
</section>
<div class="rule" style="top:1368px"></div>

<section class="events">
  <h2 class="display">Our Events</h2>
  <p>Click the button below to view and participate in upcoming events.</p>
  <div class="btn">All brewery events</div>
  <div class="hours">
    Hours of operation<br>
    Thursday - Friday: 4:00 PM - 8:00 PM<br>
    Saturday - 12:00 PM - 8:00 PM (Events 12:00 PM - 4:00 PM)<br>
    Sunday - 12:00 PM - 6:00 PM
  </div>
  <div class="art" role="img" aria-label="Illustration of a crowned figure seated on a chair holding a staff with a banner"></div>
</section>
<div class="rule" style="top:1910px"></div>

<section class="shop">
  <div class="art" role="img" aria-label="Illustration of a kneeling archer drawing a bow"></div>
  <h2 class="display">Our Shop</h2>
  <p>We brew up our passion for honest ingredients, our curiosity for different cultures, and social and environmental consciousness into characteristic beers." And "Beers with a Twist for the good of the world, for the fun of the party"</p>
  <div class="mugs" role="img" aria-label="Three mugs of beer: golden, amber and dark"></div>
</section>
<div class="rule" style="top:2405px"></div>

<section class="stories">
  <h2 class="display" style="left:98px">Our Story</h2>
  <div class="story-img" role="img" aria-label="Mural of a figure with a shield and arrow on a white wall"></div>
  <p class="story-text">Sed ut perspiciatis unde omnis iste natus error sit voluptatem accusantium dolore eque quasi architecto beatae vitae dicta sunt explicabo.</p>
  <div class="more" style="left:100px">Read more &gt;&gt;</div>

  <h2 class="display" style="left:602px">Latest Blog</h2>
  <article class="post" style="top:124px">
    <div class="thumb" role="img" aria-label="Blog photo of a painted mural"></div>
    <h4>Neque porro quisquam est qui dolorem ipsum</h4>
    <div class="meta"><span>2nd, 3rd Jan 2017</span><span>NORA BELLWEATHER</span></div>
    <p class="excerpt">Sed ut perspiciatis unde omnis iste natus error sit voluptatem accusantium dolore mque laudantium,</p>
  </article>
  <div class="post-sep" style="top:261px"></div>
  <article class="post" style="top:279px">
    <div class="thumb" role="img" aria-label="Blog photo of an archer mural"></div>
    <h4>Neque porro quisquam est qui dolorem ipsum</h4>
    <div class="meta"><span>2nd, 3rd Jan 2017</span><span>NORA BELLWEATHER</span></div>
    <p class="excerpt">Sed ut perspiciatis unde omnis iste natus error sit voluptatem accusantium dolore mque laudantium,</p>
  </article>
  <div class="post-sep" style="top:418px"></div>
  <div class="more" style="left:606px">View more &gt;&gt;</div>
</section>
<div class="rule" style="top:2909px;height:2px"></div>

<footer class="site-footer">
  <h5 class="display" style="left:98px">Harrow Lane Brewery</h5><div class="bar" style="left:98px"></div>
  <div class="f-about">
    <p>We brew up our passion for honest ingredients, our curiosity for different cultures, and social and environ mental consciousness into characteristic beers."</p>
    <p style="margin-top:12px">And "Beers with a Twist for the good of the world, for the fun of the party."</p>
  </div>

  <h5 class="display" style="left:443px">Quick Links</h5><div class="bar" style="left:443px"></div>
  <ul class="f-links">
    <li>&rsaquo; Home</li><li>&rsaquo; Our Story</li><li>&rsaquo; Brews</li><li>&rsaquo; Blog</li><li>&rsaquo; Events</li><li>&rsaquo; Contact Us</li>
  </ul>

  <h5 class="display" style="left:611px">Contact Us</h5><div class="bar" style="left:611px"></div>
  <div class="f-contact">
    <div class="row"><svg width="40" height="40" viewBox="0 0 40 40"><circle cx="20" cy="20" r="18" fill="none" stroke="#d48a14" stroke-width="2"/><path d="M20 11a6 6 0 0 0-6 6c0 5 6 12 6 12s6-7 6-12a6 6 0 0 0-6-6z" fill="none" stroke="#d48a14" stroke-width="2"/><circle cx="20" cy="17" r="2" fill="#d48a14"/></svg><b>ADDRESS,</b>Unit 4, Marlow Yard 57<br>Kiln Road London.</div>
    <div class="row"><svg width="40" height="40" viewBox="0 0 40 40"><circle cx="20" cy="20" r="18" fill="none" stroke="#d48a14" stroke-width="2"/><path d="M14 12h4l2 5-3 2a11 11 0 0 0 5 5l2-3 5 2v4c-8 2-18-8-15-15z" fill="none" stroke="#d48a14" stroke-width="2"/></svg><b>PHONE:</b>180 044 7193</div>
    <div class="row"><svg width="40" height="40" viewBox="0 0 40 40"><circle cx="20" cy="20" r="18" fill="none" stroke="#d48a14" stroke-width="2"/><rect x="12" y="14" width="16" height="12" fill="none" stroke="#d48a14" stroke-width="2"/><path d="M12 14l8 7 8-7" fill="none" stroke="#d48a14" stroke-width="2"/></svg><b>Mail:</b>info@harrowlanebrewery.com</div>
  </div>

  <h5 class="display" style="left:873px">Newsletter Signup</h5><div class="bar" style="left:873px"></div>
  <div class="f-news">
    <p>Sign Up for our newsletter</p>
    <div class="field">Email address</div>
    <div class="sub">SUBSCRIBE</div>
  </div>

  <div class="f-divider"></div>
  <p class="copy">Copyright © 2017 Harrow Lane Brewery. All Rights Reserved.</p>
  <div class="social"><span></span><span></span><span></span><span></span><span></span></div>
</footer>

</body>
</html>
```